Copper Wagon
ideas, energy & innovation
Can you also please upload drafts of the letter headed paper, compliments slips and invoice drafts for me to also look at!

```html
<!DOCTYPE html>
<html lang="en">
<head>
<meta charset="utf-8">
<title>Copper Wagon – Stationery Set</title>
<link href="https://fonts.googleapis.com/css2?family=Open+Sans:wght@400;600;700&display=swap" rel="stylesheet">
<style>
  :root{
    --bg:#e6e4e1;
    --paper:#ffffff;
    --ink:#3a3a3a;
    --muted:#8a8a8a;
    --blue:#1f6fc4;
    --blue-dark:#124f94;
    --orange:#f47a12;
    --orange-dark:#e2600a;
    --red:#d9361c;
    --green:#6cbb2b;
    --green-dark:#3f8f1c;
    --black:#1c1c1c;
    --shadow:0 2px 5px rgba(0,0,0,.28);
  }
  *{box-sizing:border-box;margin:0;padding:0}
  html,body{width:1200px;height:550px;overflow:hidden}
  body{background:var(--bg);font-family:"Open Sans",Arial,sans-serif;color:var(--ink);position:relative}
  .item{position:absolute;background:var(--paper);box-shadow:var(--shadow);overflow:hidden}
  .item svg.wave{position:absolute;left:0;bottom:0;width:100%;height:100%}
  .brand{display:flex;align-items:center;gap:4px;font-weight:700;color:var(--ink);white-space:nowrap}
  .brand .mark{display:inline-block;background:var(--blue);border-radius:2px;flex:none}

  /* business card backs */
  .card{width:172px;height:104px}
  .card .brand{position:absolute;left:9px;top:14px;font-size:10px}
  .card .brand .mark{width:10px;height:10px}
  .card .details{position:absolute;right:8px;top:9px;width:56px;font-size:4.5px;line-height:1.55;color:var(--muted)}
  .card .details .name{font-size:6px;font-weight:700;color:var(--ink)}

  /* coloured card fronts */
  .front{width:172px;height:104px;color:#fff;display:flex;flex-direction:column;align-items:center;justify-content:center;text-align:center}
  .front .brand{color:#fff;font-size:12px}
  .front .brand .mark{width:11px;height:11px;background:#fff}
  .front .line{font-size:5px;line-height:1.6;opacity:.9;margin-top:2px}
  .front .web{position:absolute;bottom:8px;font-size:5px;opacity:.9}
  .front-blue{background:radial-gradient(circle at 50% 40%,#3f93e6,var(--blue-dark))}
  .front-orange{background:radial-gradient(circle at 50% 40%,#ffa23a,var(--orange-dark))}
  .front-green{background:radial-gradient(circle at 50% 40%,#8fd84a,var(--green-dark))}

  /* letter sheets */
  .sheet{width:202px;height:312px;top:43px}
  .sheet .brand{position:absolute;left:12px;top:16px;font-size:10px}
  .sheet .brand .mark{width:10px;height:10px}
  .sheet .address{position:absolute;right:10px;top:12px;width:54px;font-size:4.5px;line-height:1.5;color:var(--muted)}
  .fax-title{position:absolute;right:14px;top:62px;font-size:12px;font-weight:700;letter-spacing:1px}
  .fax-fields{position:absolute;left:16px;right:16px;top:84px;display:grid;grid-template-columns:1fr 1fr;gap:5px 10px;font-size:4.5px;color:var(--muted)}
  .fax-fields span{border-bottom:1px solid #ccc;padding-bottom:1px}
  .sheet .foot{position:absolute;left:12px;bottom:7px;font-size:4px;color:#fff}

  /* envelopes */
  .env-small{left:602px;top:384px;width:200px;height:96px}
  .env-small .brand{position:absolute;left:9px;top:9px;font-size:8px}
  .env-small .brand .mark{width:8px;height:8px}
  .env-small .sender{position:absolute;left:9px;top:22px;font-size:4px;color:var(--muted)}
  .env-small .window{position:absolute;left:60px;top:50px;width:82px;height:20px;border:1px solid #d4d4d4;border-radius:2px}
  .env-stack{position:absolute;left:893px;top:43px;width:200px;height:437px}
  .env-stack svg{position:absolute;inset:0;filter:drop-shadow(0 2px 3px rgba(0,0,0,.3))}
  .env-top .brand{position:absolute;left:10px;top:10px;font-size:9px}
  .env-top .brand .mark{width:9px;height:9px}
  .env-top .sender{position:absolute;left:10px;top:25px;font-size:4px;line-height:1.5;color:var(--muted)}
</style>
</head>
<body>

<!-- business card backs, column one -->
<div class="item card" style="left:29px;top:38px">
  <svg class="wave" viewBox="0 0 172 104" preserveAspectRatio="none"><path d="M0 82 C60 62 115 100 172 72 L172 104 L0 104Z" fill="var(--green)"/><path d="M0 76 C60 58 115 94 172 66 L172 72 C115 100 60 62 0 82Z" fill="var(--orange)"/></svg>
  <div class="brand"><span class="mark"></span>CopperWagon</div>
  <div class="details"><div class="name">Daniel Hart</div>Sales Lead<br>Tel 555 0142<br>Fax 555 0143<br>mail@copperwagon.com</div>
</div>
<div class="item card" style="left:29px;top:156px">
  <svg class="wave" viewBox="0 0 172 104" preserveAspectRatio="none"><path d="M0 82 C60 62 115 100 172 72 L172 104 L0 104Z" fill="var(--black)"/><path d="M0 76 C60 58 115 94 172 66 L172 72 C115 100 60 62 0 82Z" fill="var(--green)"/></svg>
  <div class="brand"><span class="mark"></span>CopperWagon</div>
  <div class="details"><div class="name">Daniel Hart</div>Sales Lead<br>Tel 555 0142<br>Fax 555 0143<br>mail@copperwagon.com</div>
</div>
<div class="item card" style="left:29px;top:268px">
  <svg class="wave" viewBox="0 0 172 104" preserveAspectRatio="none"><path d="M0 82 C60 62 115 100 172 72 L172 104 L0 104Z" fill="var(--blue)"/><path d="M0 76 C60 58 115 94 172 66 L172 72 C115 100 60 62 0 82Z" fill="var(--green)"/></svg>
  <div class="brand"><span class="mark"></span>CopperWagon</div>
  <div class="details"><div class="name">Daniel Hart</div>Sales Lead<br>Tel 555 0142<br>Fax 555 0143<br>mail@copperwagon.com</div>
</div>

<!-- business card backs, column two -->
<div class="item card" style="left:216px;top:38px">
  <svg class="wave" viewBox="0 0 172 104" preserveAspectRatio="none"><path d="M0 82 C60 62 115 100 172 72 L172 104 L0 104Z" fill="var(--red)"/><path d="M0 76 C60 58 115 94 172 66 L172 72 C115 100 60 62 0 82Z" fill="var(--orange)"/></svg>
  <div class="brand"><span class="mark"></span>CopperWagon</div>
  <div class="details"><div class="name">Daniel Hart</div>Sales Lead<br>Tel 555 0142<br>Fax 555 0143<br>mail@copperwagon.com</div>
</div>
<div class="item card" style="left:216px;top:156px">
  <svg class="wave" viewBox="0 0 172 104" preserveAspectRatio="none"><path d="M0 82 C60 62 115 100 172 72 L172 104 L0 104Z" fill="var(--orange)"/><path d="M0 76 C60 58 115 94 172 66 L172 72 C115 100 60 62 0 82Z" fill="var(--black)"/></svg>
  <div class="brand"><span class="mark"></span>CopperWagon</div>
  <div class="details"><div class="name">Daniel Hart</div>Sales Lead<br>Tel 555 0142<br>Fax 555 0143<br>mail@copperwagon.com</div>
</div>
<div class="item card" style="left:216px;top:268px">
  <svg class="wave" viewBox="0 0 172 104" preserveAspectRatio="none"><path d="M0 82 C60 62 115 100 172 72 L172 104 L0 104Z" fill="var(--green)"/><path d="M0 76 C60 58 115 94 172 66 L172 72 C115 100 60 62 0 82Z" fill="var(--blue)"/></svg>
  <div class="brand"><span class="mark"></span>CopperWagon</div>
  <div class="details"><div class="name">Daniel Hart</div>Sales Lead<br>Tel 555 0142<br>Fax 555 0143<br>mail@copperwagon.com</div>
</div>

<!-- business card fronts -->
<div class="item front front-blue" style="left:29px;top:377px">
  <div class="brand"><span class="mark"></span>CopperWagon</div>
  <div class="line">ideas, energy &amp; innovation<br>12 Mill Road, Ashby</div>
  <div class="web">www.copperwagon.com</div>
</div>
<div class="item front front-orange" style="left:216px;top:377px">
  <div class="brand"><span class="mark"></span>CopperWagon</div>
  <div class="line">ideas, energy &amp; innovation<br>12 Mill Road, Ashby</div>
  <div class="web">www.copperwagon.com</div>
</div>
<div class="item front front-green" style="left:403px;top:377px">
  <div class="brand"><span class="mark"></span>CopperWagon</div>
  <div class="line">ideas, energy &amp; innovation<br>12 Mill Road, Ashby</div>
  <div class="web">www.copperwagon.com</div>
</div>

<!-- letterhead -->
<div class="item sheet letterhead" style="left:405px">
  <div class="brand"><span class="mark"></span>CopperWagon</div>
  <div class="address">12 Mill Road<br>Ashby AB1 2CD<br>Tel 555 0142<br>Fax 555 0143<br>mail@copperwagon.com</div>
  <svg class="wave" viewBox="0 0 202 312" preserveAspectRatio="none"><path d="M0 296 C70 280 130 306 202 286 L202 312 L0 312Z" fill="var(--black)"/><path d="M0 290 C70 276 130 300 202 280 L202 286 C130 306 70 280 0 296Z" fill="var(--green)"/><path d="M0 286 C70 272 130 295 202 276 L202 280 C130 300 70 276 0 290Z" fill="var(--orange)"/></svg>
  <div class="foot">www.copperwagon.com</div>
</div>

<!-- fax sheet -->
<div class="item sheet fax" style="left:629px">
  <div class="brand"><span class="mark"></span>CopperWagon</div>
  <div class="address">12 Mill Road<br>Ashby AB1 2CD<br>Tel 555 0142<br>Fax 555 0143<br>mail@copperwagon.com</div>
  <div class="fax-title">FAX</div>
  <div class="fax-fields"><span>To</span><span>From</span><span>Fax</span><span>Pages</span><span>Phone</span><span>Date</span><span>Re</span><span>CC</span></div>
  <svg class="wave" viewBox="0 0 202 312" preserveAspectRatio="none"><path d="M0 296 C70 280 130 306 202 286 L202 312 L0 312Z" fill="var(--black)"/><path d="M0 290 C70 276 130 300 202 280 L202 286 C130 306 70 280 0 296Z" fill="var(--blue)"/><path d="M0 286 C70 272 130 295 202 276 L202 280 C130 300 70 276 0 290Z" fill="var(--red)"/></svg>
  <div class="foot">www.copperwagon.com</div>
</div>

<!-- small envelope -->
<div class="item env-small">
  <div class="brand"><span class="mark"></span>CopperWagon</div>
  <div class="sender">12 Mill Road, Ashby AB1 2CD</div>
  <div class="window"></div>
</div>

<!-- envelope stack -->
<div class="env-stack">
  <svg viewBox="0 0 288 485" width="200" height="437" preserveAspectRatio="none">
    <path d="M0 392 L288 392 L288 485 L0 485Z" fill="var(--green)"/>
    <path d="M0 392 L144 470 L288 392Z" fill="var(--green-dark)"/>
    <path d="M0 320 L288 320 L288 400 L144 440 L0 400Z" fill="var(--orange)"/>
    <path d="M0 320 L288 320 L144 410Z" fill="var(--orange-dark)"/>
    <path d="M0 250 L288 250 L288 330 L144 372 L0 330Z" fill="var(--blue)"/>
    <path d="M0 250 L288 250 L144 340Z" fill="var(--blue-dark)"/>
    <path d="M0 190 L288 190 L288 262 L144 300 L0 262Z" fill="#f6f6f6"/>
    <path d="M0 190 L288 190 L144 272Z" fill="#ffffff" stroke="#ddd" stroke-width="1"/>
    <path d="M0 118 L288 118 L288 200 L144 236 L0 200Z" fill="var(--black)"/>
    <path d="M0 118 L288 118 L144 210Z" fill="#333"/>
    <rect x="0" y="0" width="288" height="128" fill="#ffffff"/>
    <path d="M0 114 C90 100 190 126 288 106 L288 128 L0 128Z" fill="var(--green)"/>
    <path d="M0 110 C90 96 190 121 288 101 L288 106 C190 126 90 100 0 114Z" fill="var(--orange)"/>
  </svg>
  <div class="env-top">
    <div class="brand"><span class="mark"></span>CopperWagon</div>
    <div class="sender">12 Mill Road, Ashby AB1 2CD<br>www.copperwagon.com</div>
  </div>
</div>

</body>
</html>
```